Tarnwick Dwelling Crafters

We are a building company based in Melbourne Australia. We have a logo but would like to make it a bit more interesting using the same colour scheme of Black, Red and Silver. I have attached our current business card.

Reason: The designs submitted so far are not really what we are looking for. They seem a bit too corporate and we are looking for something a bit funkier.

This is a stationary design I found on the web which we like the look of, something like this using our colours of black, red and silver is what we are looking for.

Cheers

This is our current logo, and front of our business card.

Thanks

Hopefully this example stationery can be viewed to give designers an idea of the look we are hoping for.

Reason: I would like an extra few days for all designers to have the opportunity to submit their designs.

Building

eb2027
000000
aaaaaa

```html
<!DOCTYPE html>
<html lang="en">
<head>
<meta charset="utf-8">
<title>Tarnwick Dwelling Crafters</title>
<link href="https://fonts.googleapis.com/css2?family=Roboto+Condensed:wght@400&display=swap" rel="stylesheet">
<style>
  :root {
    --red: #eb2027;
    --silver: #aaaaaa;
    --black: #000000;
    --board-mid: #2e2e2e;
    --board-edge: #1c1c1c;
  }
  html, body {
    margin: 0;
    padding: 0;
    width: 1200px;
    height: 786px;
    overflow: hidden;
    background: var(--black);
  }
  .card {
    position: relative;
    width: 1200px;
    height: 786px;
    overflow: hidden;
    font-family: "Roboto Condensed", "Arial Narrow", sans-serif;
  }
  .timber-backdrop {
    position: absolute;
    inset: 0;
    background: radial-gradient(ellipse at 50% 35%, #363636 0%, var(--board-mid) 45%, var(--board-edge) 100%);
  }
  .brand {
    position: absolute;
    left: 0;
    width: 100%;
    top: 282px;
    display: flex;
    justify-content: center;
    align-items: center;
    gap: 22px;
    margin: 0;
  }
  .brand-name {
    font-size: 140px;
    line-height: 1;
    font-weight: 400;
    color: var(--silver);
  }
  .brand-square {
    width: 26px;
    height: 26px;
    background: var(--red);
    align-self: flex-start;
    margin-top: 14px;
  }
  .tagline {
    position: absolute;
    right: 64px;
    top: 672px;
    margin: 0;
    font-size: 46px;
    line-height: 1;
    font-weight: 400;
    color: var(--red);
  }
  .base-band {
    position: absolute;
    left: 0;
    bottom: 0;
    width: 100%;
    height: 14px;
    background: var(--silver);
  }
</style>
</head>
<body>
  <div class="card">
    <div class="timber-backdrop" role="img" aria-label="Dark charcoal timber board texture"></div>

    <h1 class="brand">
      <span class="brand-name">Tarnwick</span>
      <span class="brand-square" aria-hidden="true"></span>
    </h1>

    <p class="tagline">Tarnwick Dwelling Crafters</p>

    <div class="base-band"></div>
  </div>
</body>
</html>
```